Roofing Company Realtor Marketing Flyer

We would like a design for marketing material aimed at realtors. We are seeking to build relationships with local realtors to ensure that both sellers and buyers are happy and confident with their roofing systems through roof inspections, No-Leak certification, roof repairs, and replacements if necessary.

There are three points that must be included:
1. Home inspectors are generalists. We are roof experts that specialize in diagnosing and fixing roofing problems.
2. We offer "No Leak" certification to offer peace of mind to homeowners.
3. We offer referral bonuses for realtors.

Target Market(s)

Realtors

Industry/Entity Type

Roofing

Font styles to use
Sans Serif

Colors

Designer to choose colors to be used in the design.

Requirements
Must have
• Must be double-sided.
• Must be similar to current marketing materials design. See website http://shinglecrestpro.com and attached images for details.
• We would also like a "fanned out" version of our Sample Inspection Report showing glimpses of some of the images on the later pages (See attached documents).

```html
<!DOCTYPE html>
<html lang="en">
<head>
<meta charset="utf-8">
<title>ShingleCrest Pro – Realtor Flyer</title>
<link href="https://fonts.googleapis.com/css2?family=Open+Sans:wght@400;600;700;800&family=Open+Sans+Condensed:wght@300&display=swap" rel="stylesheet">
<style>
  :root{
    --orange:#f0821e;
    --charcoal:#4a4a4a;
    --ink:#222;
    --grey-mid:#9a9a9a;
    --page:#f1f1f1;
    --swoosh:#3a3a3a;
  }
  *{box-sizing:border-box;margin:0;padding:0}
  html,body{width:707px;height:1200px;overflow:hidden;background:var(--page);font-family:"Open Sans",Arial,sans-serif}
  .flyer-stage{position:relative;width:707px;height:1200px}
  .flyer{
    position:absolute;left:0;top:143px;width:535px;height:692px;
    transform:scale(1.3215);transform-origin:0 0;
    background:#fff;overflow:hidden;box-shadow:0 2px 8px rgba(0,0,0,.18);
  }
  .header-bg{position:absolute;inset:0 0 auto 0;height:150px;background:linear-gradient(180deg,#fff 0%,#e2e2e2 100%)}
  .hero{position:absolute;left:0;top:0;width:535px;height:335px}
  .brand{
    position:absolute;right:24px;top:44px;
    font-weight:400;font-size:31px;letter-spacing:-.5px;color:var(--charcoal);line-height:40px;
  }
  .section-title{
    position:absolute;top:343px;left:0;width:100%;text-align:center;
    font-size:19px;font-weight:400;line-height:26px;color:var(--ink);
  }
  .section-title span{display:inline-block;border-bottom:1.5px solid var(--grey-mid);padding:0 2px 0}
  .section-title b{color:var(--orange);font-weight:700}
  .services{position:absolute;top:389px;left:29px;width:469px;display:flex}
  .service{flex:1;display:flex;flex-direction:column;align-items:center;position:relative}
  .service + .service::before{content:"";position:absolute;left:0;top:-7px;height:102px;width:1px;background:linear-gradient(180deg,transparent,#888 50%,transparent)}
  .service-icon{width:60px;height:60px}
  .service-label{margin-top:7px;height:28px;display:flex;align-items:flex-end;text-align:center;font-size:10px;font-weight:600;line-height:14px;color:var(--ink)}
  .headline{position:absolute;top:495px;left:0;width:100%;text-align:center;color:var(--orange);font-weight:800;font-size:19.5px;line-height:24px}
  .subline{position:absolute;top:517px;left:0;width:100%;text-align:center;font-size:11px;line-height:14px;color:var(--ink)}
  .offer-pill{
    position:absolute;top:544px;left:197px;width:140px;height:28px;border-radius:6px;
    background:linear-gradient(180deg,#6a6a6a 0%,#1e1e1e 55%,#000 100%);
    color:#fff;font-weight:800;font-size:19px;text-align:center;line-height:28px;letter-spacing:.5px;
  }
  .offer-text{position:absolute;top:577px;left:0;width:100%;text-align:center;font-size:12.5px;font-weight:600;line-height:18px;color:var(--ink)}
  .offer-text em{font-style:normal;color:var(--orange)}
  .footer{position:absolute;left:0;top:610px;width:535px;height:82px}
  .phone{position:absolute;top:640px;left:0;width:100%;text-align:center;color:#fff;font-weight:600;font-size:20px;line-height:26px}
  .phone svg{vertical-align:-3px;margin-right:6px}
  .web{position:absolute;top:669px;left:0;width:100%;text-align:center;color:#fff;font-size:11px;line-height:16px}
  .web span{border-top:1px solid rgba(255,255,255,.7);padding:0 6px}
</style>
</head>
<body>
<div class="flyer-stage">
  <article class="flyer">
    <div class="header-bg"></div>

    <svg class="hero" viewBox="0 0 535 335">
      <defs>
        <linearGradient id="roofTone" x1="0" y1="0" x2="1" y2="1">
          <stop offset="0" stop-color="#8a5a3c"/>
          <stop offset=".55" stop-color="#6e4a33"/>
          <stop offset="1" stop-color="#c2955f"/>
        </linearGradient>
      </defs>
      <polygon points="0,112 155,17 325,122 535,122 535,150 325,150 155,48 0,150" fill="var(--orange)"/>
      <polygon points="0,120 155,25 325,130 535,130 535,135 325,135 155,30 0,125" fill="#fff"/>
      <g role="img" aria-label="Photo of a roof inspector in a hard hat checking a shingle roof ridge">
        <polygon points="0,150 155,48 325,150 535,150 535,335 0,335" fill="url(#roofTone)"/>
      </g>
    </svg>

    <div class="brand">ShingleCrest Pro</div>

    <h2 class="section-title"><span><b>What</b> We Do?</span></h2>

    <div class="services">
      <div class="service">
        <svg class="service-icon" viewBox="0 0 62 62"><circle cx="31" cy="31" r="30" fill="var(--orange)"/><circle cx="31" cy="31" r="26" fill="none" stroke="#fff" stroke-width="1.2" opacity=".6"/>
          <path d="M17 32 L29 21 L41 32 M21 30 V43 H37 V30" fill="#fff"/><circle cx="39" cy="24" r="5" fill="none" stroke="#fff" stroke-width="2.2"/><path d="M42.5 27.5 L47 32" stroke="#fff" stroke-width="2.6" stroke-linecap="round"/></svg>
        <div class="service-label">ROOF<br>INSPECTIONS</div>
      </div>
      <div class="service">
        <svg class="service-icon" viewBox="0 0 62 62"><circle cx="31" cy="31" r="30" fill="var(--orange)"/><circle cx="31" cy="31" r="26" fill="none" stroke="#fff" stroke-width="1.2" opacity=".6"/>
          <circle cx="31" cy="27" r="11" fill="none" stroke="#fff" stroke-width="2.4"/><path d="M26 27 L30 31 L36 23" fill="none" stroke="#fff" stroke-width="2.4" stroke-linecap="round"/><path d="M24 37 L21 47 L26 44 L28 48 L31 38 M38 37 L41 47 L36 44 L34 48 L31 38" fill="#fff"/></svg>
        <div class="service-label">NO-LEAK<br>CERTIFICATION</div>
      </div>
      <div class="service">
        <svg class="service-icon" viewBox="0 0 62 62"><circle cx="31" cy="31" r="30" fill="var(--orange)"/><circle cx="31" cy="31" r="26" fill="none" stroke="#fff" stroke-width="1.2" opacity=".6"/>
          <path d="M15 40 L31 22 L47 36 V44 H15 Z" fill="#fff"/><path d="M27 19 L37 29" stroke="#fff" stroke-width="3" stroke-linecap="round"/><rect x="33" y="14" width="8" height="6" transform="rotate(45 37 17)" fill="#fff"/></svg>
        <div class="service-label">ROOF REPAIRS</div>
      </div>
      <div class="service">
        <svg class="service-icon" viewBox="0 0 62 62"><circle cx="31" cy="31" r="30" fill="var(--orange)"/><circle cx="31" cy="31" r="26" fill="none" stroke="#fff" stroke-width="1.2" opacity=".6"/>
          <path d="M15 40 L31 24 L47 40" fill="none" stroke="#fff" stroke-width="3.2" stroke-linecap="round"/><path d="M19 44 L31 32 L43 44" fill="none" stroke="#fff" stroke-width="2.4" stroke-linecap="round"/><path d="M40 17 V25 M36 21 H44" stroke="#fff" stroke-width="2.4" stroke-linecap="round"/></svg>
        <div class="service-label">REPLACEMENTS</div>
      </div>
    </div>

    <h1 class="headline">HOME INSPECTORS ARE GENERALISTS</h1>
    <p class="subline">We are roof experts that specialize in diagnosing and fixing roofing problems</p>

    <div class="offer-pill">WE OFFER</div>
    <p class="offer-text"><em>No Leak</em> certification to offer peace of mind to homeowners.<br>Referral bonuses for realtors.</p>

    <svg class="footer" viewBox="0 0 535 82" aria-hidden="true">
      <path d="M0 36 Q250 -14 535 28 V82 H0 Z" fill="var(--swoosh)"/>
      <path d="M0 42 Q250 -4 535 34 V82 H0 Z" fill="#fff"/>
      <path d="M0 48 Q250 4 535 40 V82 H0 Z" fill="var(--orange)"/>
    </svg>
    <div class="phone"><svg width="18" height="18" viewBox="0 0 24 24"><path d="M6.6 10.8a15 15 0 0 0 6.6 6.6l2.2-2.2a1 1 0 0 1 1-.25 11.4 11.4 0 0 0 3.6.57 1 1 0 0 1 1 1V20a1 1 0 0 1-1 1A17 17 0 0 1 3 4a1 1 0 0 1 1-1h3.5a1 1 0 0 1 1 1c0 1.25.2 2.45.57 3.6a1 1 0 0 1-.25 1z" fill="#fff"/><path d="M15 3a6 6 0 0 1 6 6M15 6.5A2.5 2.5 0 0 1 17.5 9" stroke="#fff" stroke-width="1.6" fill="none"/></svg>555-310-4827</div>
    <div class="web"><span>◉ www.shinglecrestpro.com</span></div>
  </article>
</div>
</body>
</html>
```